Driving School Business card design

Hi, we are starting a new business (Driving School) and would like your help with our business card design.
We are located in Adelaide SA.
Our aim is to help young people achieve best possible results by promoting safe and stress free driving.

Name of our school is "Velmira" which means best or most favorable.

Hope there is someone out there in wonderful world of design who can think outside of square and give us recognizable/ unique business card design.

Target Market(s)

16+

Industry/Entity Type

Business

Contact Information for Business Card

Name of our business is "Velmira driver training"
Our idea is to make letter "L' in Velmira more distinct (noticeable) by different color or font, so it gets associated with learner driver.
We like combination of white, dark gray and yellow but do not limit our self to that.
Reverse side of our card would have to incorporate writing space for date and time of the next lesson.

Requirements
Must have
• Business name: Velmira driver training
• Owner/ instructor name
• Mobile no:
• Chatterloop logo
Should not have
• Anything Not associated with driving

```html
<!DOCTYPE html>
<html lang="en">
<head>
<meta charset="utf-8">
<title>Velmira driver training – business card</title>
<link rel="stylesheet" href="https://fonts.googleapis.com/css2?family=Open+Sans:wght@400;600;700&display=swap">
<style>
  :root {
    --backdrop: #3b322e;
    --card-black: #0e0e0e;
    --card-white: #ffffff;
    --brand-yellow: #fbec3f;
    --brand-grey: #6b6b6b;
    --text-light: #f2f2f2;
    --text-dark: #4a4a4a;
    --rule: #8a8a8a;
  }
  * { box-sizing: border-box; margin: 0; padding: 0; }
  html, body {
    width: 1200px;
    height: 900px;
    overflow: hidden;
    background: var(--backdrop);
    font-family: "Open Sans", Arial, sans-serif;
  }
  .card-set {
    position: absolute;
    inset: 0;
    display: flex;
    align-items: center;
    justify-content: center;
    gap: 40px;
  }
  .card {
    position: relative;
    width: 540px;
    height: 310px;
    overflow: hidden;
    box-shadow: 0 10px 30px rgba(0,0,0,0.45);
  }

  /* Front */
  .card-front {
    background: var(--card-black);
    display: flex;
    flex-direction: column;
    align-items: center;
    justify-content: center;
  }
  .brand {
    display: flex;
    align-items: center;
    gap: 14px;
    margin-bottom: 14px;
  }
  .brand-dot {
    width: 58px;
    height: 58px;
    border-radius: 50%;
    background: var(--brand-yellow);
  }
  .brand-name {
    color: var(--brand-grey);
    font-weight: 600;
    text-transform: uppercase;
    line-height: 1;
  }
  .brand-name .word-main { display: block; font-size: 50px; letter-spacing: 1px; }
  .brand-name .word-sub { display: block; font-size: 14px; letter-spacing: 5px; margin-top: 4px; }
  .owner-name {
    color: var(--brand-yellow);
    font-weight: 700;
    font-size: 24px;
    margin-bottom: 10px;
  }
  .contact-list { list-style: none; color: var(--text-light); font-size: 16px; }
  .contact-list li { display: flex; align-items: center; gap: 8px; margin-bottom: 4px; }
  .contact-icon { width: 12px; height: 12px; flex: none; }
  .social-name {
    margin-top: 10px;
    color: var(--text-light);
    font-size: 14px;
    font-weight: 600;
  }

  /* Back */
  .card-back { background: var(--card-white); }
  .back-shape { position: absolute; inset: 0; }
  .appointment {
    position: absolute;
    left: 290px;
    top: 46px;
    width: 225px;
    color: var(--text-dark);
  }
  .appointment-title {
    font-size: 19px;
    font-weight: 600;
    padding-bottom: 6px;
    border-bottom: 2px dotted var(--rule);
    margin-bottom: 26px;
  }
  .appointment-field {
    display: flex;
    align-items: flex-end;
    font-size: 13px;
    margin-bottom: 30px;
  }
  .appointment-field .fill { flex: 1; border-bottom: 2px dotted var(--rule); margin: 0 3px 3px; }
</style>
</head>
<body>
  <main class="card-set">
    <section class="card card-front" aria-label="Card front">
      <div class="brand">
        <span class="brand-dot"></span>
        <p class="brand-name"><span class="word-main">Velmira</span><span class="word-sub">Driver Training</span></p>
      </div>
      <h1 class="owner-name">Darren Kessler</h1>
      <ul class="contact-list">
        <li>
          <svg class="contact-icon" viewBox="0 0 12 12"><rect x="3" y="0.5" width="6" height="11" rx="1.2" fill="none" stroke="#fbec3f" stroke-width="1.4"/></svg>
          044-987 654 321
        </li>
        <li>
          <svg class="contact-icon" viewBox="0 0 12 12"><circle cx="6" cy="6" r="5.2" fill="#fbec3f"/></svg>
          www.velmiradriving.com
        </li>
      </ul>
      <p class="social-name">Chatterloop</p>
    </section>

    <section class="card card-back" aria-label="Card back">
      <svg class="back-shape" viewBox="0 0 540 310" width="540" height="310">
        <circle cx="-20" cy="330" r="320" fill="#6b6b6b"/>
        <circle cx="-20" cy="345" r="285" fill="#fbec3f"/>
        <rect x="0" y="0" width="18" height="310" fill="#6b6b6b"/>
      </svg>
      <div class="appointment">
        <h2 class="appointment-title">Your Next Appointment is</h2>
        <p class="appointment-field">Date: <span class="fill"></span></p>
        <p class="appointment-field">Time: <span class="fill"></span>AM<span class="fill"></span>PM</p>
      </div>
    </section>
  </main>
</body>
</html>
```